MediDesk 4.2 is web based clinic management software. We require 1 logo for the software product, login page design and landing page (patient queue) design. The design should include all elements required logo, icons , buttons and type faces. http://md2021.tralvonix.my/Default.aspxTest login : KQ417 password : 4826 Final output should be in psd for developer to convert to css for web application.

Number of Pages Required

1 page

Colors

Designer to choose colors to be used in the design.

Requirements
Must have
• Product Logo , icon, login page design, and 1 main page design as attached.

```html
<!DOCTYPE html>
<html lang="en">
<head>
<meta charset="utf-8">
<title>MediDesk – Login and Queue List</title>
<link href="https://fonts.googleapis.com/css2?family=Mulish:wght@400;600;700;800&display=swap" rel="stylesheet">
<style>
:root{
  --navy:#0d3a78;
  --teal-navy:#1b5f8c;
  --brand:#0b5cad;
  --brand-deep:#0a4f9c;
  --sky:#3fb1f5;
  --pill:#1593e6;
  --green:#3ec47c;
  --green-link:#2fbf71;
  --ink:#333b44;
  --muted:#8a9099;
  --line:#dde1e6;
  --panel:#f2f3f4;
  --white:#ffffff;
}
*{box-sizing:border-box;margin:0;padding:0}
html,body{width:976px;height:1200px;overflow:hidden}
body{font-family:"Mulish",sans-serif;color:var(--ink);position:relative}
.backdrop{position:absolute;inset:0;
  background:linear-gradient(180deg,#1a6fcb 0%,#1c8ed4 30%,#22a8cf 45.5%,#1a6fcb 45.5%,#1c8fd2 75%,#24b0d4 100%)}
.abs{position:absolute}

/* Login card */
.login-card{left:170px;top:93px;width:634px;height:361px;border-radius:13px;overflow:hidden;background:var(--white);box-shadow:0 10px 30px rgba(0,40,90,.25)}
.login-aside{left:0;top:0;width:317px;height:361px;background:linear-gradient(160deg,#0c63b8,#0a4f9f);color:var(--white)}
.aside-title{right:45px;top:56px;text-align:right;font-weight:800;font-size:28px;line-height:27px}
.aside-title .tag{font-size:12px;font-weight:700;color:var(--sky);margin-right:6px}
.aside-mark{left:133px;top:226px;width:50px;height:50px;border-radius:50%;background:var(--pill)}
.aside-note{left:0;width:317px;top:281px;text-align:center;font-size:10px;line-height:13px}
.aside-mail{left:0;width:317px;top:323px;text-align:center;font-size:10.5px;color:var(--sky)}
.login-form{left:317px;top:0;width:317px;height:361px}
.brand{display:flex;align-items:center;gap:6px;font-size:27px;font-weight:700;color:var(--brand)}
.brand .dot{width:12px;height:12px;border-radius:50%;background:var(--sky)}
.login-form .brand{left:53px;top:60px}
.login-lead{left:53px;top:99px;width:170px;font-size:10px;line-height:13px;color:var(--muted)}
.field{left:53px;width:210px;height:34px;border:1px solid var(--line);border-radius:17px;padding:0 17px;display:flex;align-items:center;justify-content:space-between;font-size:10px;color:#555}
.field svg{width:10px;height:10px;fill:#a3a8ae}
.btn-login{left:53px;top:246px;width:112px;height:34px;border-radius:17px;background:linear-gradient(90deg,#0d6ac2,#0a4f9c);color:var(--white);font-size:10px;font-weight:800;letter-spacing:1.3px;display:flex;align-items:center;justify-content:space-between;padding:0 20px}
.link-clear{left:181px;top:258px;font-size:9.5px;letter-spacing:1.2px;color:var(--pill);text-decoration:underline}
.form-foot{left:53px;top:326px;font-size:8.5px;color:var(--muted);display:flex;gap:23px}

/* Dashboard */
.dashboard{left:40px;top:589px;width:896px;height:569px;border-radius:13px;overflow:hidden;background:var(--panel);box-shadow:0 10px 30px rgba(0,40,90,.25)}
.sidebar{left:0;top:0;width:174px;height:569px;background:linear-gradient(180deg,var(--navy),var(--teal-navy));color:var(--white)}
.sidebar .brand{left:0;width:174px;top:32px;justify-content:center;font-size:17px;color:var(--white)}
.sidebar .brand .dot{width:8px;height:8px}
.avatar{left:62px;top:72px;width:48px;height:48px;border-radius:50%;background:linear-gradient(135deg,#c99a7a,#6b4a3a);border:2px solid var(--green)}
.doctor{left:0;width:174px;top:129px;text-align:center;font-size:8.5px;font-weight:600}
.nav-active{left:0;top:173px;width:174px;height:29px;background:rgba(255,255,255,.1)}
.nav-item{left:34px;font-size:9.5px}
.nav-group{left:34px;width:112px;font-size:9.5px;color:var(--sky);display:flex;justify-content:space-between;align-items:center}
.nav-group svg{width:7px;height:7px;stroke:var(--white);fill:none;stroke-width:1.6}
.divider{left:0;width:174px;height:1px;background:rgba(255,255,255,.12)}

.page-title{left:190px;top:32px;font-size:20px;font-weight:400;color:#222}
.link-new{left:308px;top:40px;font-size:10px;font-weight:700;color:var(--green-link);text-decoration:underline}
.user-mail{left:677px;top:39px;font-size:10px;color:#444}
.btn-logout{left:773px;top:33px;width:90px;height:26px;border-radius:13px;background:linear-gradient(90deg,#1593e6,#0b5cad);color:var(--white);font-size:8px;font-weight:800;letter-spacing:1px;display:flex;align-items:center;justify-content:space-between;padding:0 12px 0 17px}
.arrow{width:10px;height:10px;stroke:currentColor;fill:none;stroke-width:1.6}
.filter-label{top:103px;font-size:9px;color:#333}
.select{top:95px;height:26px;border-radius:13px;background:var(--pill);color:var(--white);font-size:8.5px;display:flex;align-items:center;justify-content:space-between;padding:0 12px 0 18px}
.select svg{width:8px;height:8px;stroke:var(--white);fill:none;stroke-width:1.6}

.tabs-line{left:198px;top:192px;width:679px;height:1px;background:var(--line)}
.tab{top:164px;height:29px;display:flex;align-items:center;font-size:9.5px;font-weight:700}
.tab.active{left:198px;width:97px;background:var(--white);color:var(--pill);justify-content:center;border:1px solid var(--line);border-bottom:none}
.tab.idle{left:313px;color:#444}
.col{font-size:8.5px}
.head{top:213px;color:#666;letter-spacing:.2px}
.row{left:196px;width:681px;height:42px;background:var(--white);border-radius:2px}
.row .col{position:absolute;top:15px;color:#333}
.btn-view{position:absolute;left:588px;top:10px;width:81px;height:23px;border-radius:2px;background:var(--green);color:var(--white);font-size:8.5px;font-weight:700;display:flex;align-items:center;justify-content:center}
</style>
</head>
<body>
<div class="backdrop" role="img" aria-label="Blue tinted snowy mountain landscape background"></div>

<section class="login-card abs">
  <div class="login-aside abs" role="img" aria-label="Blue tinted photo of a stethoscope and laptop on a desk">
    <h1 class="aside-title abs"><span class="tag">Web based</span>Clinic<br>management<br>software</h1>
    <div class="aside-mark abs"></div>
    <p class="aside-note abs">MediDesk 4.2 is web based clinic<br>management software.</p>
    <p class="aside-mail abs">info@halvreth.com</p>
  </div>
  <div class="login-form abs">
    <div class="brand abs"><span>MediDesk</span><span class="dot"></span></div>
    <p class="login-lead abs">Please enter your username and password to login.</p>
    <div class="field abs" style="top:147px"><span>Username</span>
      <svg viewBox="0 0 10 10"><circle cx="5" cy="3" r="2.2"/><path d="M1 10a4 4 0 0 1 8 0z"/></svg></div>
    <div class="field abs" style="top:197px"><span>Password</span>
      <svg viewBox="0 0 10 10"><path d="M3 4.5V3a2 2 0 0 1 4 0v1.5h-1V3a1 1 0 0 0-2 0v1.5z"/><rect x="2" y="4.5" width="6" height="5" rx="1"/></svg></div>
    <div class="btn-login abs"><span>LOGIN</span><svg class="arrow" viewBox="0 0 10 10"><path d="M1 5h8M5.5 1.5 9 5l-3.5 3.5"/></svg></div>
    <span class="link-clear abs">CLEAR</span>
    <div class="form-foot abs"><span>Forgot your login?</span><span>Privacy Policy</span></div>
  </div>
</section>

<section class="dashboard abs">
  <aside class="sidebar abs">
    <div class="brand abs"><span>MediDesk</span><span class="dot"></span></div>
    <div class="avatar abs" role="img" aria-label="Doctor profile photo"></div>
    <p class="doctor abs">DR. Name Goes Here</p>
    <div class="nav-active abs"></div>
    <span class="nav-item abs" style="top:181px">Queue</span>
    <span class="nav-item abs" style="top:211px">Patient</span>
    <span class="nav-item abs" style="top:242px">Visit Entry</span>
    <span class="nav-item abs" style="top:272px">Payment</span>
    <div class="divider abs" style="top:310px"></div>
    <div class="nav-group abs" style="top:333px"><span>Claims Invoice</span><svg viewBox="0 0 8 8"><path d="M1 2.5 4 5.5 7 2.5"/></svg></div>
    <span class="nav-item abs" style="top:363px">Standard</span>
    <span class="nav-item abs" style="top:394px">Wizard-style</span>
    <span class="nav-item abs" style="top:424px">Bulk</span>
    <span class="nav-item abs" style="top:454px">Flat</span>
    <div class="divider abs" style="top:494px"></div>
    <div class="nav-group abs" style="top:516px"><span>Maintenance</span><svg viewBox="0 0 8 8"><path d="M2.5 1 5.5 4 2.5 7"/></svg></div>
  </aside>

  <h2 class="page-title abs">Queue List</h2>
  <span class="link-new abs">New Queue</span>
  <span class="user-mail abs">info@halvreth.com</span>
  <div class="btn-logout abs"><span>LOGOUT</span><svg class="arrow" viewBox="0 0 10 10"><path d="M1 5h8M5.5 1.5 9 5l-3.5 3.5"/></svg></div>

  <span class="filter-label abs" style="left:195px">Show</span>
  <div class="select abs" style="left:236px;width:88px"><span>All Status</span><svg viewBox="0 0 8 8"><path d="M1 2.5 4 5.5 7 2.5"/></svg></div>
  <span class="filter-label abs" style="left:353px">From</span>
  <div class="select abs" style="left:389px;width:106px"><span>19 Nov 2018</span><svg viewBox="0 0 8 8"><path d="M1 2.5 4 5.5 7 2.5"/></svg></div>
  <span class="filter-label abs" style="left:527px">to</span>
  <div class="select abs" style="left:548px;width:106px"><span>19 Nov 2018</span><svg viewBox="0 0 8 8"><path d="M1 2.5 4 5.5 7 2.5"/></svg></div>
  <span class="filter-label abs" style="left:679px">Location</span>
  <div class="select abs" style="left:728px;width:88px"><span>All Facilities</span><svg viewBox="0 0 8 8"><path d="M1 2.5 4 5.5 7 2.5"/></svg></div>

  <div class="tabs-line abs"></div>
  <div class="tab active abs">New Patient</div>
  <div class="tab idle abs">Existing Patient</div>

  <span class="col head abs" style="left:196px">Sr. No</span>
  <span class="col head abs" style="left:275px">Patient Name</span>
  <span class="col head abs" style="left:398px">MR Number</span>
  <span class="col head abs" style="left:505px">Medication</span>
  <span class="col head abs" style="left:601px">Appt. Date</span>
  <span class="col head abs" style="left:706px">Appt. Time</span>

  <div class="row abs" style="top:233px"><span class="col" style="left:16px">01</span><span class="col" style="left:79px">Name Goes Here</span><span class="col" style="left:202px">0123456789</span><span class="col" style="left:309px">Dummy name</span><span class="col" style="left:405px">19 Nov 2018</span><span class="col" style="left:508px">10:40 AM</span><span class="btn-view">View Details</span></div>
  <div class="row abs" style="top:283px"><span class="col" style="left:16px">02</span><span class="col" style="left:79px">Name Goes Here</span><span class="col" style="left:202px">0123456789</span><span class="col" style="left:309px">Dummy name</span><span class="col" style="left:405px">19 Nov 2018</span><span class="col" style="left:508px">10:40 AM</span><span class="btn-view">View Details</span></div>
  <div class="row abs" style="top:332px"><span class="col" style="left:16px">03</span><span class="col" style="left:79px">Name Goes Here</span><span class="col" style="left:202px">0123456789</span><span class="col" style="left:309px">Dummy name</span><span class="col" style="left:405px">19 Nov 2018</span><span class="col" style="left:508px">10:40 AM</span><span class="btn-view">View Details</span></div>
  <div class="row abs" style="top:382px"><span class="col" style="left:16px">04</span><span class="col" style="left:79px">Name Goes Here</span><span class="col" style="left:202px">0123456789</span><span class="col" style="left:309px">Dummy name</span><span class="col" style="left:405px">19 Nov 2018</span><span class="col" style="left:508px">10:40 AM</span><span class="btn-view">View Details</span></div>
  <div class="row abs" style="top:431px"><span class="col" style="left:16px">05</span><span class="col" style="left:79px">Name Goes Here</span><span class="col" style="left:202px">0123456789</span><span class="col" style="left:309px">Dummy name</span><span class="col" style="left:405px">19 Nov 2018</span><span class="col" style="left:508px">10:40 AM</span><span class="btn-view">View Details</span></div>
</section>
</body>
</html>
```